Business card needed for the Vantro of Dry Cleaning!

We need a slick business card design for a new company based out of Montreal called PliZip Lockers (in French) and Pli&Zip Lockers inc. (in English). We're the Vantro of Laundry. We offer services of dry cleaning, laundry (wash&fold), minor clothing alterations, shoe repair and parcel delivery through 24/7 secured and connected lockers. Ordres are placed through our mobile application. Real time notification are sent to customers when their order is ready for pickup. The lockers will be placed throughout the downtown area, in condo and office towers, where a high density of busy people converge. It is simple, user-friendly, and most importantly convenient. We're the out of the box dry cleaner, literally.
Updates

Target Market(s)

1) Professional workers wearing suits daily
2) Campus students living in residences
3) People using laundromats
4) Families with children/yuppies who prefer to use their time doing something else than laundry

Industry/Entity Type

Dry Cleaning

Contact Information for Business Card

Name / Sylvie-Anne Berthiaume
Title / CEO & Founder
Company Name / PliZip Lockers | Pli&Zip Lockers inc.
Website www.plizip.ca

Requirements
Must have
• Text Logo: Pli&Zip - Nettoyeurs 24/7 Cleaners
• Logo on one side and contact info on the other (bilingual)
• Minimalist, pure design
• "We care" for your belongings feeling
• Professional, technological, clean & fresh look
Should not have
• No busy visuals. No rainbow colors.

```html
<!DOCTYPE html>
<html lang="en">
<head>
<meta charset="utf-8">
<title>PliZip Lockers Business Card</title>
<link rel="stylesheet" href="https://fonts.googleapis.com/css2?family=Open+Sans:wght@400;600&family=Arimo:wght@400;700&display=swap">
<style>
  :root {
    --backdrop: #333b40;
    --card: #ffffff;
    --band: #302a33;
    --accent: #1a8fd6;
    --ink: #2b2530;
    --splash: #d6ebf7;
  }
  * { margin: 0; padding: 0; box-sizing: border-box; }
  html, body { width: 1200px; height: 789px; overflow: hidden; }
  body { background: var(--backdrop); position: relative; font-family: "Open Sans", sans-serif; color: var(--ink); }

  .card {
    position: absolute; top: 224px; width: 556px; height: 342px;
    background: var(--card); overflow: hidden;
  }
  .card--front { left: 30px; }
  .card--back { left: 613px; }

  .card__band { position: absolute; left: 0; top: 0; width: 32px; height: 100%; background: var(--band); }
  .card__stripe { position: absolute; left: 33px; top: 0; width: 5px; height: 100%; background: var(--accent); }

  .card__splash {
    position: absolute; width: 230px; height: 200px; right: -20px; bottom: 10px;
    border-radius: 50%;
    background: radial-gradient(circle at 45% 50%, var(--splash) 0 36%, rgba(214,235,247,0.5) 48%, rgba(214,235,247,0) 70%);
  }
  .card--back .card__splash { right: 10px; bottom: 40px; }

  .wordmark {
    position: absolute; display: flex; align-items: center; gap: 12px;
    font-family: "Open Sans", sans-serif; font-weight: 400;
    font-size: 38px; line-height: 52px; letter-spacing: -0.5px; color: var(--ink); white-space: nowrap;
  }
  .wordmark__dot { width: 14px; height: 14px; border-radius: 50%; background: var(--accent); flex: none; }
  .card--front .wordmark { left: 67px; top: 34px; }
  .card--back .wordmark { left: 124px; top: 245px; }

  .person { position: absolute; left: 67px; top: 178px; }
  .person__name { font-size: 19px; line-height: 26px; }
  .person__title { font-size: 15px; color: var(--accent); line-height: 20px; }

  .contact { position: absolute; left: 67px; top: 241px; list-style: none; font-size: 15.5px; }
  .contact li { display: flex; align-items: center; height: 22px; }
  .contact svg { width: 12px; height: 14px; margin-right: 15px; fill: var(--accent); }
  .contact .contact__plain { padding-left: 27px; }

  .offer { position: absolute; left: 0; right: 0; font-family: "Arimo", sans-serif; color: var(--ink); }
  .offer__heading { font-weight: 700; font-size: 15.5px; text-align: center; letter-spacing: 0.3px; }
  .services { top: 38px; }
  .services ul { list-style: none; margin: 3px 0 0 175px; font-size: 16px; letter-spacing: 0.6px; line-height: 20.5px; }
  .services li::before { content: "\2022"; margin-right: 6px; }
  .delivery { top: 163px; text-align: center; }
  .delivery p { font-size: 16px; letter-spacing: 0.6px; margin-top: 2px; }
</style>
</head>
<body>
  <section class="card card--front" aria-label="Card front">
    <div class="card__splash" role="img" aria-label="Soft light blue paint splash decoration"></div>
    <div class="card__band"></div>
    <div class="card__stripe"></div>
    <div class="wordmark"><span>PliZip Lockers</span><span class="wordmark__dot"></span></div>
    <div class="person">
      <p class="person__name">Sylvie-Anne Berthiaume</p>
      <p class="person__title">CEO &amp; Founder</p>
    </div>
    <ul class="contact">
      <li><svg viewBox="0 0 10 14"><rect x="1" y="0" width="8" height="14" rx="1.5"/><rect x="2.5" y="2" width="5" height="8" fill="#fff"/></svg>000.000.0000</li>
      <li><svg viewBox="0 0 12 10"><rect x="0" y="1" width="12" height="8" rx="1"/><path d="M0 1.5 L6 6 L12 1.5" stroke="#fff" stroke-width="1.2" fill="none"/></svg>info@plizip.ca</li>
      <li class="contact__plain">www.plizip.ca</li>
    </ul>
  </section>

  <section class="card card--back" aria-label="Card back">
    <div class="card__splash" role="img" aria-label="Soft light blue paint splash decoration"></div>
    <div class="card__band"></div>
    <div class="card__stripe"></div>
    <div class="offer services">
      <h2 class="offer__heading">SERVICES</h2>
      <ul>
        <li>Dry Cleaning</li>
        <li>Laundry (wash&amp;fold)</li>
        <li>Minor Clothing Alterations</li>
        <li>Shoe Repair</li>
      </ul>
    </div>
    <div class="offer delivery">
      <h2 class="offer__heading">PARCEL DELIVERY</h2>
      <p>Through 24/7 Secured And Connected Lockers</p>
    </div>
    <div class="wordmark"><span>PliZip Lockers</span><span class="wordmark__dot"></span></div>
  </section>
</body>
</html>
```